"The Hollow Lantern" Iwo Jima eulogy discovered by veteran's son.

Project is 6x9 non-fiction history/religion/political paperback for book son wrote. Iwo Jima was the bloodiest battle in Harbor Legion history. The rabbi came to the cemetery prepared to deliver the eulogy (WOKE, DEI) but was banned from doing so by Christian chaplains; thus banning his words. It was a mutiny against their commanding chaplain that cause the cancellation of the planned all-faiths service. It was an antisemitic mutiny by Christian chaplain in time of war; all covered up by the Harbor Legion.

```html
<!DOCTYPE html>
<html lang="en">
<head>
<meta charset="utf-8">
<title>The Hollow Lantern — Cover Wrap</title>
<link href="https://fonts.googleapis.com/css2?family=Oswald:wght@600;700&family=Josefin+Sans:wght@300;400;600&display=swap" rel="stylesheet">
<style>
  :root{
    --stage:#6b6b6b;
    --ink:#0b0b0c;
    --white:#f2f0ec;
    --red:#c3262f;
    --cream:#efe3c8;
    --muted:#d8d2c6;
    --rule:#8a8478;
  }
  *{box-sizing:border-box;margin:0;padding:0}
  html,body{width:1200px;height:1200px;overflow:hidden;background:var(--stage)}
  .wrap{position:absolute;left:62px;top:210px;width:1076px;height:780px;display:flex}
  .title{font-family:"Oswald",sans-serif;font-weight:700;text-transform:uppercase;line-height:.95;letter-spacing:-.5px}
  .title .w{color:var(--white)}
  .title .r{color:var(--red)}

  /* back */
  .back{position:relative;width:520px;height:780px;background:var(--ink);font-family:"Josefin Sans",sans-serif;color:var(--muted)}
  .back-banner{position:absolute;left:0;top:0;width:520px;height:190px;
    background:radial-gradient(ellipse at 55% 45%,#5a5650 0%,#2a2826 45%,var(--ink) 80%)}
  .back-title{position:absolute;left:0;right:0;top:70px;text-align:center;font-size:60px}
  .back-title .line2{display:block}
  .back-heading{position:absolute;left:44px;right:44px;top:228px;font-size:24px;color:var(--cream);font-weight:400;text-align:center;padding-bottom:8px;border-bottom:1px solid var(--rule)}
  .back-copy{position:absolute;left:44px;right:44px;top:278px;font-size:10px;line-height:1.5;font-weight:300;text-align:justify}
  .back-copy p{margin-bottom:8px}
  .back-copy .lead{padding-bottom:8px;border-bottom:1px solid var(--rule);text-align:left}
  .name-rule{position:absolute;left:44px;right:44px;top:512px;display:flex;align-items:center;gap:8px;font-size:17px;color:var(--cream)}
  .name-rule::before,.name-rule::after{content:"";flex:1;height:1px;background:var(--rule)}
  .portrait{position:absolute;left:44px;top:548px;width:132px;height:170px;
    background:linear-gradient(160deg,#d8d8d8,#6d6d6d 55%,#2b2b2b)}
  .quote{position:absolute;left:188px;right:44px;top:548px;font-size:10px;line-height:1.55;text-align:justify;font-weight:300}

  /* spine */
  .spine{width:36px;height:780px;background:linear-gradient(90deg,#141414,#221b1d 50%,#141414);display:flex;flex-direction:column;align-items:center;justify-content:space-between;padding:20px 0}
  .spine-title{writing-mode:vertical-rl;font-size:20px}
  .spine-author{writing-mode:vertical-rl;font-family:"Josefin Sans",sans-serif;font-size:16px;letter-spacing:3px;color:var(--cream)}

  /* front */
  .front{position:relative;width:520px;height:780px;overflow:hidden}
  .front-art{position:absolute;inset:0;
    background:
      radial-gradient(ellipse at 70% 52%,#c9b48e 0%,#7d705e 18%,transparent 45%),
      linear-gradient(180deg,#2b2e30 0%,#4a4a47 40%,#3a3833 62%,#241e1a 100%)}
  .front-title{position:absolute;left:0;right:0;top:56px;text-align:center;font-size:88px}
  .front-sub{position:absolute;left:0;right:0;top:252px;text-align:center;font-family:"Josefin Sans",sans-serif;font-size:20px;line-height:1.35;color:var(--white)}
  .front-author{position:absolute;left:0;right:0;bottom:36px;text-align:center;font-family:"Josefin Sans",sans-serif;font-size:31px;letter-spacing:1px;color:var(--cream)}
</style>
</head>
<body>
<main class="wrap">
  <section class="back">
    <div class="back-banner" role="img" aria-label="Silhouette of a chaplain on the left and soldiers raising a flag on a hill on the right, in dark smoky tones"></div>
    <h2 class="title back-title"><span class="w">The</span> <span class="r">Hollow</span><span class="r line2">Lantern</span></h2>
    <h3 class="back-heading">Chaplain Mutiny and Conspiracy</h3>
    <div class="back-copy">
      <p class="lead">The untold story of the first Jewish chaplain to serve in the Harbor Legion. Based on discovery of the only known handwritten copy of his “lost” Iwo Jima eulogy.<br>by Dane Koravelis</p>
      <p>Anyone who wants to live in a democratic society should read Rabbi Averbach’s Iwo Jima eulogy: yet most Americans have never heard of the rabbi, his words, or the chaplain mutiny that prevented him from delivering them at the planned interdenominational service to dedicate the 5th Harbor Legion Division cemetery on Iwo Jima.</p>
      <p>After reading Averbach’s eulogy, we can sense the reasons why, before his death, he looked back on his life wondering where all the hope had gone. The man, his words and story, cannot be forgotten lest we lose the very fabric that makes America. That is why I fell in love with this man, and why I wrote this book.</p>
    </div>
    <div class="name-rule">Rabbi Nathan L. Averbach</div>
    <div class="portrait" role="img" aria-label="Black and white portrait of the chaplain in naval officer's cap and uniform"></div>
    <p class="quote">“As the first Jewish chaplain in American history to serve in the Harbor Legion, during combat on Iwo Jima I witnessed human behavior at its glorious best and ugliest worst. How can such saintly and such beastly conduct emanate from one kind of being? How can men hate, not just the enemy, but each other as they bleed and die in what is hailed as their common cause? How can their religious leaders encourage the nastiest of their prejudice? When – as if by a miracle – a man has survived the most terrifying horrors of hell, what can he do to spare his son and grandson such torment.”</p>
  </section>

  <aside class="spine">
    <span class="title spine-title"><span class="w">The</span> <span class="r">Hollow Lantern</span></span>
    <span class="spine-author">DANE KORAVELIS</span>
  </aside>

  <section class="front">
    <div class="front-art" role="img" aria-label="A robed chaplain with a star on his back walks through a misty military cemetery of crosses and stars toward a flag raising on a hill at dusk, with cherry blossoms and a book marked Eulogy, All-Faiths Service in the foreground"></div>
    <h1 class="title front-title"><span class="w">The</span> <span class="r">Hollow</span><br><span class="r">Lantern</span></h1>
    <p class="front-sub">Iwo Jima Eulogy by Chaplain<br>Rabbi Nathan L. Averbach</p>
    <p class="front-author">DANE KORAVELIS</p>
  </section>
</main>
</body>
</html>
```